Mobile App UI for Telecommunications/Hosting Company

We are about to convert our existing self-service Customer Portal into a mobile phone application and need an elegant and professional UI/UX design. Our company provides telecommunication (voice/mobile/data) and hosting services to medium-sized business. The primary purpose of the application is to view trouble tickets, alerts, orders, and performance charts. This application is available to customers only - not the general public.

Please provide a UI design suitable for display on iPhone/Android devices. The attached document includes a proposed screen flow. You are free to design your own screens to display the same information elegantly.
Updates

Please note that the design should be based on the wireframes in the Word document, not the screenshots.  The screenshots are just to show our existing web portal look & feel.

Also, just a few screens are required for initial submission (3 would be great).

Thanks,
Dermot.

Target Market(s)

IT Managers away from their desk and using a mobile phone application.
Adult males from technical background aged 30-50.
Customers of Brindlewood Networks have access to this application (not the general public). This is a self-service portal for customers only.

Industry/Entity Type

Business

Colors
0592cd
33a6d7
85cae6
cadf82
fde08a

Requirements
Must have
• Please look at the screenshots from our current Customer Portal site (part of the project brief). The mobile app does not have to look the same, but should follow a similar style.

Please check out our company web site at www.brindlewoodnetworks.example (this site is not the customer portal and has a different look at feel) to understand what Brindlewood Networks does.
Nice to have
• Sharing capabilities via email/SMS.
A nice background image to make it stand out
The colours selected below are a guide only as they are similar to the corporate colours
- The priority is something that works on a phone - a design extendable to tablets is a nice to have as our existing web site looks OK on a tablet..

```html
<!DOCTYPE html>
<html lang="en">
<head>
<meta charset="utf-8">
<title>Brindlewood Networks – Customer Portal Home</title>
<link rel="stylesheet" href="https://fonts.googleapis.com/css2?family=Open+Sans:ital,wght@0,400;0,600;0,700;1,400&display=swap">
<style>
  :root {
    --brand-blue: #0592cd;
    --mid-blue: #33a6d7;
    --sky-blue: #85cae6;
    --panel: #eef3f6;
    --row: #e3e8eb;
    --row-active: #d7dcdf;
    --divider: #cfd6da;
    --ink: #3a3f44;
    --ink-soft: #555b60;
    --white: #ffffff;
    --status: #000000;
    --page: #f4f6f7;
  }
  * { box-sizing: border-box; margin: 0; padding: 0; }
  html, body { width: 730px; height: 1200px; overflow: hidden; background: var(--page); }
  body { font-family: "Open Sans", Arial, sans-serif; color: var(--ink); }

  .app {
    position: absolute; left: 29px; top: 4px;
    width: 672px; height: 1192px;
    background: var(--panel);
    display: flex; flex-direction: column;
    overflow: hidden;
  }

  .status-bar {
    height: 39px; background: var(--status); color: var(--white);
    display: flex; align-items: center; justify-content: space-between;
    padding: 0 10px; font-weight: 700; font-size: 25px;
  }
  .status-bar .carrier { display: flex; align-items: flex-end; gap: 6px; }
  .signal { display: flex; align-items: flex-end; gap: 2px; height: 16px; }
  .signal span { width: 4px; background: var(--white); }
  .status-bar .icons { display: flex; gap: 12px; align-items: center; }

  .toolbar {
    height: 91px; background: var(--sky-blue);
    display: flex; align-items: flex-start; padding: 14px 31px 0;
    gap: 20px;
  }
  .toolbar .spacer { flex: 1; }
  .tool-btn {
    width: 87px; height: 62px; background: var(--brand-blue);
    display: flex; align-items: center; justify-content: center;
    box-shadow: 0 2px 0 rgba(0,0,0,0.08);
  }

  .brand-bar {
    height: 125px; background: var(--white);
    display: flex; align-items: center; justify-content: center; gap: 18px;
  }
  .brand-name { font-size: 34px; font-weight: 400; color: var(--ink); letter-spacing: -0.5px; }
  .brand-dot { width: 52px; height: 52px; border-radius: 50%; background: var(--mid-blue); }

  .section-title {
    height: 71px; background: var(--brand-blue); color: var(--white);
    font-size: 31px; font-weight: 700; padding-left: 29px;
    display: flex; align-items: center;
  }
  .section-sub {
    height: 59px; background: var(--sky-blue); color: var(--white);
    font-size: 24px; font-weight: 600; padding-left: 29px;
    display: flex; align-items: center;
  }

  .news-item {
    height: 150px; background: var(--panel);
    border-bottom: 1px solid var(--divider);
    display: flex; padding: 32px 0 0 32px; gap: 22px;
  }
  .news-item:last-child { border-bottom: none; }
  .news-thumb {
    width: 106px; height: 81px; flex: none;
    background: linear-gradient(135deg, #d9eef8, #9fd3ec);
    border: 1px solid var(--divider);
  }
  .news-title { font-style: italic; font-weight: 400; font-size: 17px; color: var(--brand-blue); margin-top: -2px; }
  .news-meta { font-size: 13.5px; color: var(--ink-soft); line-height: 21px; margin-top: 11px; }

  .list-row {
    height: 63px; background: var(--row);
    border-bottom: 1px solid var(--divider);
    display: flex; align-items: center; padding-left: 14px;
    font-size: 15px; color: var(--ink-soft); white-space: nowrap;
  }
  .list-row .chev { font-size: 14px; margin-right: 9px; color: var(--ink-soft); }
  .list-row strong { color: var(--ink); font-weight: 600; margin-right: 4px; }
  .list-row.is-active { background: var(--row-active); color: var(--brand-blue); }
  .list-row.is-active .chev, .list-row.is-active strong { color: var(--brand-blue); font-weight: 400; }
  .list-row.is-cut { height: 50px; align-items: flex-end; padding-bottom: 6px; border-bottom: none; }

  .tab-bar { height: 83px; display: flex; background: var(--sky-blue); margin-top: auto; }
  .tab {
    display: flex; align-items: center; justify-content: center;
    font-size: 20px; font-weight: 600; color: #2e3a42;
    border-left: 1px solid rgba(255,255,255,0.45);
  }
  .tab:first-child { border-left: none; }
  .tab.is-current { background: var(--brand-blue); color: var(--white); }
</style>
</head>
<body>
<main class="app">
  <div class="status-bar">
    <div class="carrier">
      <div class="signal"><span style="height:6px"></span><span style="height:8px"></span><span style="height:11px"></span><span style="height:13px"></span><span style="height:16px"></span></div>
      <span>Carrow</span>
    </div>
    <span>4:20 PM</span>
    <div class="icons">
      <svg width="22" height="22" viewBox="0 0 22 22"><circle cx="11" cy="11" r="10" fill="#fff"/><path d="M11 5v6h4" stroke="#000" stroke-width="2" fill="none"/></svg>
      <svg width="22" height="22" viewBox="0 0 22 22"><path d="M21 1 1 10l9 2 2 9z" fill="#fff"/></svg>
      <svg width="28" height="26" viewBox="0 0 28 26"><path d="M22 13a9 9 0 1 1-3-6.7" stroke="#fff" stroke-width="2.5" fill="none"/><path d="M17 3l5 3-4 4" fill="#fff"/><rect x="9" y="11" width="9" height="7" fill="#fff"/><path d="M11 11V9a2.5 2.5 0 0 1 5 0v2" stroke="#fff" stroke-width="2" fill="none"/></svg>
      <svg width="44" height="20" viewBox="0 0 44 20"><rect x="1" y="2" width="38" height="16" rx="2" stroke="#fff" stroke-width="2" fill="none"/><rect x="4" y="5" width="32" height="10" fill="#fff"/><rect x="40" y="7" width="3" height="6" fill="#fff"/></svg>
    </div>
  </div>

  <nav class="toolbar">
    <div class="tool-btn" aria-label="Quick actions">
      <svg width="30" height="40" viewBox="0 0 30 40"><path d="M19 1 3 23h10l-3 16L27 16H16z" fill="#fff"/></svg>
    </div>
    <div class="tool-btn" aria-label="Switch camera">
      <svg width="60" height="34" viewBox="0 0 60 34"><rect x="18" y="7" width="24" height="17" rx="3" fill="#fff"/><rect x="25" y="3" width="10" height="5" fill="#fff"/><circle cx="30" cy="15.5" r="5" fill="#0592cd"/><path d="M14 14c-8 2-10 6-4 9 6 3 24 4 36 1" stroke="#fff" stroke-width="3" fill="none"/><path d="M44 20l6 4-7 3z" fill="#fff"/><path d="M46 12c6 1 8 3 6 5" stroke="#fff" stroke-width="3" fill="none"/></svg>
    </div>
    <div class="spacer"></div>
    <div class="tool-btn" aria-label="Locate">
      <svg width="40" height="40" viewBox="0 0 40 40"><circle cx="20" cy="20" r="12" stroke="#fff" stroke-width="3.5" fill="none"/><circle cx="20" cy="20" r="3" fill="#fff"/><path d="M20 2v10M20 28v10M2 20h10M28 20h10" stroke="#fff" stroke-width="3.5"/></svg>
    </div>
    <div class="tool-btn" aria-label="Close">
      <svg width="30" height="30" viewBox="0 0 30 30"><path d="M3 3l24 24M27 3 3 27" stroke="#fff" stroke-width="5"/></svg>
    </div>
  </nav>

  <header class="brand-bar">
    <span class="brand-name">brindlewood networks</span>
    <span class="brand-dot" aria-hidden="true"></span>
  </header>

  <h1 class="section-title">Brindlewood News</h1>
  <section class="news-list">
    <article class="news-item">
      <div class="news-thumb" role="img" aria-label="News article thumbnail"></div>
      <div>
        <h2 class="news-title">A heartwarming response to a life-saving surgery</h2>
        <p class="news-meta">By Owen Talbridge (Brindlewood Networks), Tuesday 25th March 2014<br>15-year-old Milo Carranza, our latest sponsored</p>
      </div>
    </article>
    <article class="news-item">
      <div class="news-thumb" role="img" aria-label="News article thumbnail"></div>
      <div>
        <h2 class="news-title">A heartwarming response to a life-saving surgery</h2>
        <p class="news-meta">By Owen Talbridge (Brindlewood Networks), Tuesday 25th March 2014<br>15-year-old Milo Carranza, our latest sponsored</p>
      </div>
    </article>
  </section>

  <h2 class="section-sub">Event Feed</h2>
  <div class="list-row is-active"><span class="chev">»</span><strong>7/2 11:00</strong> - Ticket 343(MVDC1234) has been resolved.</div>
  <div class="list-row"><span class="chev">»</span><strong>7/2 11:00</strong> - MPDCL123456 Sydnly is unavailable.</div>
  <div class="list-row is-cut"><span class="chev">»</span><strong>7/2 11:00</strong> - A note was added to ticket 343</div>

  <h2 class="section-sub">Recently Accessed</h2>
  <div class="list-row"><span class="chev">»</span>T343-NBAR not showing in MFRS21315006</div>
  <div class="list-row"><span class="chev">»</span>T674670- Not receiving patching alerts</div>
  <div class="list-row"><span class="chev">»</span>0139844- redundancy links for SIP project</div>

  <nav class="tab-bar">
    <div class="tab is-current" style="width:126px">Ticket</div>
    <div class="tab" style="width:116px">Alerts</div>
    <div class="tab" style="width:123px">Orders</div>
    <div class="tab" style="width:136px">Services</div>
    <div class="tab" style="width:171px">Contact Us</div>
  </nav>
</main>
</body>
</html>
```